Stationary and Business Card Design for Harrow Lane Tailoring House, LLC
What is a Harrow Lane? A man that that timeless style and uncompromising taste.
Stationary and Business Card Design for Harrow Lane Tailoring House, LLC - Apparel
Creative Brief
Professional
Norma T. Vickery
Chief Executive Officer
873 Pilbeck Lane Fernwick, MD 20614
nvickery@harrowlanetailor.example
www.harrowlanetailor.example
Logo on the back of business card What is a Harrow Lane? A man that that timeless style and uncompromising taste.
tdvoss7 tdvoss7
Back of the business card needs to change "service offered" to "Custom Services Offered:"
Subtitle #1 What is a Harrow Lane? A man that timeless style and uncompromising taste. Subtitle #2 You can never be overtrained or overdressed. Suit up for success.
can you also provide different color options: silver background with purple font, silver background with blue font, black background with silver font, blue background with silver font.
Please remove the address line. Please submit business card designs with only the cursive letter logos on the front side. Back side of the business card will list our services offered as such: Services Offered: Suits Waist Coats Pea Coats Business Coats Fashion Consulting Subtitle has an error listed. We would like to see how another subtitle looks on the card to aid in our final choice for our slogan. Subtitle #1 What is a Harrow Lane? A man that that timeless style and uncompromising taste. Subtitle #2 You can never be overtrained or overdressed. Suit up for success.

```html
<!DOCTYPE html>
<html lang="en">
<head>
<meta charset="utf-8">
<title>Harrow Lane Tailoring House – Business Card</title>
<link rel="stylesheet" href="https://fonts.googleapis.com/css2?family=Cormorant+Garamond:ital,wght@0,500;1,500&family=Open+Sans:wght@400;600&display=swap">
<style>
  :root {
    --page: #e9e6e1;
    --navy: #0f1a2e;
    --navy-deep: #0b1424;
    --black: #0c0c0d;
    --silver: #d4d6da;
    --silver-soft: #b9bcc2;
    --swoosh: #8a8e96;
    --swoosh-light: #b4b7bd;
    --shadow: rgba(0, 0, 0, 0.35);
  }
  * { box-sizing: border-box; margin: 0; padding: 0; }
  html, body {
    width: 1200px;
    height: 900px;
    overflow: hidden;
    background: var(--page);
  }
  .canvas {
    position: relative;
    width: 1200px;
    height: 900px;
  }
  .card {
    position: absolute;
    left: 280px;
    width: 640px;
    height: 366px;
    border-radius: 22px;
    overflow: hidden;
    box-shadow: 0 14px 30px var(--shadow);
    color: var(--silver);
  }
  .card--back { top: 60px; background: var(--navy); }
  .card--front { top: 470px; background: var(--navy); }

  .brand {
    position: absolute;
    left: 0;
    right: 0;
    text-align: center;
    font-family: "Cormorant Garamond", serif;
    font-weight: 500;
    font-size: 25px;
    letter-spacing: 2.5px;
    text-transform: uppercase;
    color: var(--silver);
  }
  .card--back .brand { top: 86px; }
  .card--front .brand { top: 62px; }

  .services {
    position: absolute;
    left: 0;
    right: 0;
    top: 168px;
    text-align: center;
    font-family: "Cormorant Garamond", serif;
    font-style: italic;
    font-weight: 500;
    color: var(--silver);
    line-height: 1.25;
  }
  .services__title { font-size: 21px; }
  .services__list { font-size: 20px; }
  .services__slogan { font-size: 20px; margin-top: 2px; }

  .wave {
    position: absolute;
    inset: 0;
    width: 100%;
    height: 100%;
  }

  .person {
    position: absolute;
    left: 34px;
    top: 176px;
    font-family: "Open Sans", sans-serif;
    color: var(--silver-soft);
  }
  .person__name { font-size: 22px; font-weight: 600; color: var(--silver); }
  .person__role { font-size: 15px; margin-top: 2px; }

  .contact {
    position: absolute;
    right: 26px;
    bottom: 26px;
    list-style: none;
    font-family: "Open Sans", sans-serif;
    font-size: 16px;
    color: var(--silver);
    text-align: right;
  }
  .contact__item {
    display: flex;
    align-items: center;
    justify-content: flex-end;
    gap: 12px;
    height: 27px;
  }
  .contact__icon { width: 16px; height: 16px; flex: none; }
</style>
</head>
<body>
<main class="canvas">

  <section class="card card--back" aria-label="Business card back">
    <p class="brand">Harrow Lane Tailoring House, LLC</p>
    <div class="services">
      <p class="services__title">Custom Services Offered</p>
      <p class="services__list">Suits|Tuxedos|Waist Coats|Business Coats|Pea Coats</p>
      <p class="services__slogan">You can never be overtrained or overdressed. Suit up for success.</p>
    </div>
  </section>

  <section class="card card--front" aria-label="Business card front">
    <svg class="wave" viewBox="0 0 640 366" preserveAspectRatio="none" aria-hidden="true">
      <path d="M150,118 C230,150 300,232 430,246 C520,256 590,262 640,290" fill="none" stroke="var(--swoosh)" stroke-width="12"/>
      <path d="M170,112 C250,150 320,222 450,236 C540,246 600,252 640,268" fill="none" stroke="var(--swoosh-light)" stroke-width="3"/>
      <path d="M0,150 C150,140 250,240 420,256 C520,264 600,276 640,300 L640,366 L0,366 Z" fill="var(--black)"/>
    </svg>

    <p class="brand">Harrow Lane Tailoring House, LLC</p>

    <div class="person">
      <p class="person__name">Norma T. Vickery</p>
      <p class="person__role">Chief Executive Officer</p>
    </div>

    <ul class="contact">
      <li class="contact__item">
        <span>(555)014-2297</span>
        <svg class="contact__icon" viewBox="0 0 16 16" aria-hidden="true"><rect x="4" y="1" width="8" height="14" rx="1.5" fill="none" stroke="var(--silver)" stroke-width="1.4"/><line x1="7" y1="12.5" x2="9" y2="12.5" stroke="var(--silver)" stroke-width="1.2"/></svg>
      </li>
      <li class="contact__item">
        <span>nvickery@harrowlanetailor.example</span>
        <svg class="contact__icon" viewBox="0 0 16 16" aria-hidden="true"><rect x="1" y="3" width="14" height="10" fill="var(--silver)"/><path d="M1,3 L8,9 L15,3" fill="none" stroke="var(--black)" stroke-width="1.2"/></svg>
      </li>
      <li class="contact__item">
        <span>www.harrowlanetailor.example</span>
        <svg class="contact__icon" viewBox="0 0 16 16" aria-hidden="true"><circle cx="8" cy="8" r="6.5" fill="none" stroke="var(--silver)" stroke-width="1.3"/><ellipse cx="8" cy="8" rx="2.8" ry="6.5" fill="none" stroke="var(--silver)" stroke-width="1"/><line x1="1.5" y1="8" x2="14.5" y2="8" stroke="var(--silver)" stroke-width="1"/></svg>
      </li>
    </ul>
  </section>

</main>
</body>
</html>
```